indoor tennis and sports center( club)

we need a logo for a new business venture, it will be for business cards and for presentations.
presentations for potential investors and authorities.
the design needs to communicate the sport and a community of tennis players
the center includes a tennis academy, and sports club with training sessions for all ages

Reason: so that I can get some more feedback on my side as to te design we want

Target Market(s)

potential investors or partners

Industry/Entity Type

Business

Contact Information for Business Card

i need the name of the club
names of the partners
slogan" changing lives through tennis" on the front
the clubs three main goals are ports education , academy and a community club

Colors
3176b5
33b8a4
fbee3d
0dac94
acd036

Requirements
Must have
• a strong logo
• names of the partners
• web site and email address
• tel number
Nice to have
• a connection between the different aspects of the club

```html
<!DOCTYPE html>
<html lang="en">
<head>
<meta charset="utf-8">
<title>Baseline Indoor Tennis Club – Business Cards</title>
<link rel="stylesheet" href="https://fonts.googleapis.com/css2?family=Lato:wght@400;700;900&display=swap">
<style>
  :root {
    --bg: #ece9e4;
    --card: #f7f7f7;
    --card-edge: #e2e2e2;
    --band: #c8244f;
    --band-dark: #b01e45;
    --rule: #1e1e1e;
    --ink: #222222;
    --accent: #c8244f;
  }
  * { box-sizing: border-box; margin: 0; padding: 0; }
  html, body { width: 1200px; height: 780px; overflow: hidden; }
  body {
    background: var(--bg);
    font-family: "Lato", Arial, sans-serif;
    color: var(--ink);
    position: relative;
  }
  .card {
    position: absolute;
    width: 580px;
    height: 330px;
    background: linear-gradient(135deg, #ffffff 0%, var(--card) 60%, #ededed 100%);
    border-radius: 24px;
    box-shadow: 0 2px 0 var(--card-edge), 0 10px 24px rgba(0,0,0,0.12);
    overflow: hidden;
  }
  .card--front { left: 40px; top: 50px; }
  .card--back  { left: 580px; top: 400px; }

  .band {
    position: absolute;
    top: 0; bottom: 0;
    width: 140px;
    background: linear-gradient(90deg, var(--band) 0%, var(--band-dark) 100%);
  }
  .rule {
    position: absolute;
    top: 0; bottom: 0;
    width: 3px;
    background: var(--rule);
  }
  .card--front .band { left: 100px; }
  .card--front .rule--left { left: 84px; }
  .card--front .rule--right { left: 253px; }

  .card--back .band { left: 360px; }
  .card--back .rule--left { left: 344px; }
  .card--back .rule--right { left: 513px; }

  .emblem {
    position: absolute;
    width: 184px;
    height: 184px;
    border-radius: 50%;
    background: #ffffff;
    display: flex;
    flex-direction: column;
    align-items: center;
    justify-content: center;
    text-align: center;
    color: var(--ink);
    font-weight: 700;
    font-size: 17px;
    line-height: 1.25;
    letter-spacing: 0.04em;
  }
  .card--front .emblem { left: 78px; top: 30px; }
  .card--back .emblem { left: 338px; top: 73px; }

  .contact {
    position: absolute;
    left: 285px;
    top: 120px;
    width: 270px;
  }
  .contact__name {
    font-weight: 700;
    font-size: 26px;
    letter-spacing: -0.01em;
    margin-bottom: 18px;
  }
  .contact__line {
    font-size: 14px;
    line-height: 1.5;
    white-space: nowrap;
  }
  .contact__label { color: var(--accent); font-weight: 700; }
  .contact__sep { color: var(--accent); margin: 0 4px; }
  .contact__areas {
    font-size: 17px;
    margin-top: 6px;
    white-space: nowrap;
  }

  .slogan {
    position: absolute;
    left: 40px;
    top: 150px;
    font-size: 22px;
    font-weight: 400;
    color: var(--ink);
    letter-spacing: -0.01em;
  }
</style>
</head>
<body>

  <section class="card card--front" aria-label="Business card front">
    <div class="rule rule--left"></div>
    <div class="band"></div>
    <div class="rule rule--right"></div>
    <div class="emblem">Baseline<br>Indoor Tennis<br>Club</div>

    <div class="contact">
      <p class="contact__name">DARA ELLISON</p>
      <p class="contact__line"><span class="contact__label">P:</span> 5550 123 456<span class="contact__sep">|</span><span class="contact__label">E:</span> hi@baseline.example</p>
      <p class="contact__line"><span class="contact__label">W:</span> www.baseline.example</p>
      <p class="contact__areas">Indoor club | Academy | Education</p>
    </div>
  </section>

  <section class="card card--back" aria-label="Business card back">
    <div class="rule rule--left"></div>
    <div class="band"></div>
    <div class="rule rule--right"></div>
    <div class="emblem">Baseline<br>Indoor Tennis<br>Club</div>
    <p class="slogan">Changing lives through Tennis</p>
  </section>

</body>
</html>
```